Saffron Attic

I need a vinyl banner for my tent when I do Festivals both outside and inside. The banner will be approximately 3 feet high and 5 feet long.
I will be selling vintage and antique items mainly smalls not large furniture. See pictures for the types of items I will be selling. Also vintage bar ware, KELDAN, Glassware, Halvick Ware, ect.

```html
<!DOCTYPE html>
<html lang="en">
<head>
<meta charset="UTF-8">
<title>Saffron Attic — Festival Banner</title>
<link rel="stylesheet" href="https://fonts.googleapis.com/css2?family=Allura&display=swap">
<style>
  :root {
    --banner-bg-deep: #1a0302;
    --banner-bg-warm: #2c0605;
    --bronze: #98663b;
    --ornament-strong: rgba(152, 102, 59, 0.42);
    --ornament-mid: rgba(152, 102, 59, 0.26);
    --ornament-soft: rgba(152, 102, 59, 0.12);
  }
  html, body {
    margin: 0;
    padding: 0;
    width: 1200px;
    height: 720px;
    overflow: hidden;
    background: var(--banner-bg-deep);
  }
  .banner {
    position: relative;
    width: 1200px;
    height: 720px;
    overflow: hidden;
    background: radial-gradient(ellipse at 50% 50%, var(--banner-bg-warm) 0%, var(--banner-bg-deep) 85%);
  }
  .banner__ornament {
    position: absolute;
    left: 0;
    width: 1200px;
    height: 182px;
  }
  .banner__ornament--top {
    top: 0;
    background:
      radial-gradient(ellipse 13% 100% at 50% 0%, var(--ornament-strong) 0%, var(--ornament-mid) 60%, transparent 100%),
      radial-gradient(ellipse 36% 95% at 50% 0%, var(--ornament-mid) 0%, var(--ornament-soft) 65%, transparent 100%),
      linear-gradient(to bottom, var(--ornament-soft) 0%, transparent 70%);
  }
  .banner__ornament--bottom {
    bottom: 0;
    background:
      radial-gradient(ellipse 13% 100% at 50% 100%, var(--ornament-strong) 0%, var(--ornament-mid) 60%, transparent 100%),
      radial-gradient(ellipse 36% 95% at 50% 100%, var(--ornament-mid) 0%, var(--ornament-soft) 65%, transparent 100%),
      linear-gradient(to top, var(--ornament-soft) 0%, transparent 70%);
  }
  .banner__title {
    position: absolute;
    left: 0;
    right: 0;
    top: 228px;
    margin: 0;
    text-align: center;
    font-family: "Allura", cursive;
    font-weight: 400;
    font-size: 206px;
    line-height: 1;
    color: var(--bronze);
    white-space: nowrap;
  }
</style>
</head>
<body>
  <main class="banner">
    <div class="banner__ornament banner__ornament--top" role="img" aria-label="Engraved bronze baroque scrollwork with a central medallion along the top edge"></div>
    <h1 class="banner__title">Saffron Attic</h1>
    <div class="banner__ornament banner__ornament--bottom" role="img" aria-label="Engraved bronze baroque scrollwork with a central medallion along the bottom edge"></div>
  </main>
</body>
</html>
```